Business card for a new cabinet shop company named Marlowe Cabinets for high end cabinets

Design a business card, thinking dark rich green with colours to speak of high end luxury ie; cream, gold, black possibly

Peter Lindqvar
Director Craftsman
Email: info@marlowecabinets.com.au
Instagram : @marlowe.cabinets

```html
<!DOCTYPE html>
<html lang="en">
<head>
<meta charset="utf-8">
<title>Marlowe Cabinets – Business Card</title>
<link rel="stylesheet" href="https://fonts.googleapis.com/css2?family=Montserrat:wght@500&family=Poppins:wght@300;400&display=swap">
<style>
  :root {
    --backdrop: #b3b3b3;
    --forest: #042e20;
    --forest-deep: #05261a;
    --gold: #c9a961;
    --cream: #fbf8d8;
    --ink: #000000;
    --muted: #a8a8a8;
    --white: #ffffff;
  }
  * { margin: 0; padding: 0; box-sizing: border-box; }
  html, body {
    width: 1200px; height: 1200px; overflow: hidden;
    background: var(--backdrop);
  }
  .canvas { position: relative; width: 1200px; height: 1200px; }

  .card { position: absolute; left: 207px; width: 785px; height: 471px; overflow: hidden; }
  .card-front { top: 117px; background: var(--forest); }
  .card-back { top: 652px; background: var(--cream); height: 470px; }

  .front-band {
    position: absolute; left: 0; top: 122px; width: 100%; height: 227px;
    background: var(--forest-deep);
  }
  .front-band::before, .front-band::after {
    content: ""; position: absolute; left: 0; width: 100%; height: 1px;
    background: linear-gradient(90deg, transparent, var(--gold) 15%, var(--gold) 85%, transparent);
    opacity: .7;
  }
  .front-band::before { top: 0; }
  .front-band::after { bottom: 0; }

  .brand-mark { position: absolute; border: 4px solid var(--gold); }
  .card-front .brand-mark { left: 122px; top: 162px; width: 140px; height: 140px; }
  .card-back .brand-mark { left: 62px; top: 107px; width: 82px; height: 82px; border-width: 3px; }

  .brand-name, .brand-sub {
    position: absolute; font-family: "Poppins", sans-serif; font-weight: 400;
    color: var(--gold); line-height: 1; white-space: nowrap;
  }
  .card-front .brand-name { left: 326px; top: 162px; font-size: 90px; }
  .card-front .brand-sub { left: 330px; top: 263px; font-size: 52px; letter-spacing: .28em; }
  .card-back .brand-name { left: 179px; top: 104px; font-size: 52px; }
  .card-back .brand-sub { left: 181px; top: 161px; font-size: 29px; letter-spacing: .35em; }

  .back-panel { position: absolute; inset: 0; }

  .contact { position: absolute; right: 54px; text-align: right; white-space: nowrap; line-height: 1; }
  .person-name {
    top: 231px; font-family: "Montserrat", sans-serif; font-weight: 500;
    font-size: 32px; color: var(--white); letter-spacing: .01em;
  }
  .person-role {
    top: 274px; font-family: "Poppins", sans-serif; font-weight: 400;
    font-size: 21px; color: var(--cream);
  }
  .contact-line {
    font-family: "Poppins", sans-serif; font-weight: 300; font-size: 22px; color: var(--muted);
  }
  .contact-line .label { color: var(--gold); font-weight: 400; }
  .contact-email { top: 357px; }
  .contact-social { top: 393px; }
</style>
</head>
<body>
<div class="canvas">

  <section class="card card-front" aria-label="Business card front">
    <div class="front-band"></div>
    <div class="brand-mark" aria-hidden="true"></div>
    <div class="brand-name">marlowe</div>
    <div class="brand-sub">CABINETS</div>
  </section>

  <section class="card card-back" aria-label="Business card back">
    <svg class="back-panel" width="785" height="470" viewBox="0 0 785 470" aria-hidden="true">
      <path d="M438 0 C460 78 458 165 379 232 L137 470 L785 470 L785 0 Z" fill="var(--ink)"/>
    </svg>
    <div class="brand-mark" aria-hidden="true"></div>
    <div class="brand-name">marlowe</div>
    <div class="brand-sub">CABINETS</div>

    <div class="contact person-name">PETER LINDQVAR</div>
    <div class="contact person-role">Director Craftsman</div>
    <div class="contact contact-line contact-email"><span class="label">Email:</span> info@marlowecabinets.com.au</div>
    <div class="contact contact-line contact-social"><span class="label">Instagram :</span> @marlowe.cabinets</div>
  </section>

</div>
</body>
</html>
```